Modern SaaS Dashboard Redesign for Building Management Platform

Overview:
Refer to velmora.com.au
We need a complete visual redesign of our property management dashboard to make it sleek, modern, and highly user-friendly. The current interface is functional but outdated. We want a high end SaaS design that feels intuitive, and visually engaging for daily use.

Style Direction:

Retain existing colour palette
Consistent, modern iconography and typography
Responsive design consideration (desktop-first, but adaptable to mobile)

Deliverables:
High-fidelity dashboard design in Figma or Adobe XD
Style guide for colours, typography, and icons
Layered files for developer handoff

Customer Journey Context

This dashboard is the central control panel for a property management SaaS platform (Velmora) used by building managers, strata managers, and executive committee members to manage building data and operations.

Entry Point: User logs in via the secure portal → lands directly on the dashboard.

Primary Goal: Quickly assess building portfolio health, upcoming actions, and key compliance dates.

Secondary Goal: Navigate smoothly to specific building data, reports, or contractor tasks without getting lost in menus.

Typical Flow:

Glance Phase (0–10 seconds) – User scans top stat cards for red/orange alerts or overdue actions.

Action Phase (10–30 seconds) – Clicks into urgent items from “Next Action List” or stat cards.

Work Phase (1–5 minutes) – Navigates to buildings or reports for detail work, filters/searches, and updates records.

2. Who This is For

Building Managers – Daily operational users, need fast visibility of inspections, insurance, defects, and maintenance.

Strata Managers / Property Managers – Portfolio-level oversight across multiple buildings.

Executive Committee Members (Owners Corporations) – View-only or limited-action users needing transparency and governance oversight.

Internal Support/Admin Staff – Back-office users providing data entry, compliance tracking, and troubleshooting.

3. Stakeholders Who Will See This Dashboard

Internal Admin Team – To monitor user activity and portfolio health.

Portfolio Managers – To track multiple properties at once and ensure compliance deadlines aren’t missed.

Building Service Providers – Certain contractors may have limited dashboard visibility for their assigned properties.

Compliance Officers / Auditors – May access the dashboard to verify documentation and timelines.

4. Key Design Considerations Based on Audience

Immediate clarity – Visual hierarchy that prioritises critical actions first.

Minimal learning curve – Clean, intuitive navigation with consistent patterns.

Quick search/filtering – Users may have dozens or hundreds of buildings to manage.

Mobile awareness – Many building managers work in the field, so components should adapt for tablets and smaller screens.

```html
<!DOCTYPE html>
<html lang="en">
<head>
<meta charset="utf-8">
<title>Velmora Dashboard</title>
<link href="https://fonts.googleapis.com/css2?family=Inter:wght@400;500;600;700&display=swap" rel="stylesheet">
<style>
:root{
  --page:#f9ddd1;
  --side:#fdf1ec;
  --card:#fdeee8;
  --card-line:#fff6f2;
  --search:#fcd9cc;
  --ink:#111111;
  --muted:#9a8c86;
  --line:#f3d6cb;
  --thead:#fbe2d8;
  --red-bg:#f8b4ae;--red:#b3261e;
  --amber-bg:#fde0c4;--amber:#e4a24f;
  --peach-bg:#fcd8c8;--peach:#e7a88c;
  --green-bg:#d6ecd2;--green:#7cae72;
  --black:#111111;
}
*{box-sizing:border-box;margin:0;padding:0}
html,body{width:1200px;height:467px;overflow:hidden}
body{font-family:"Inter",sans-serif;background:var(--page);color:var(--ink);position:relative}

.sidebar{position:absolute;left:0;top:0;width:151px;height:467px;background:var(--side);border-right:1px solid #f1dfd7}
.brand{position:absolute;left:14px;top:17px;display:flex;align-items:center;gap:6px;font-weight:700;font-size:13px}
.brand-dot{width:16px;height:16px;border-radius:50%;background:var(--ink)}
.nav{position:absolute;left:14px;top:58px;width:123px;list-style:none}
.nav li{display:flex;align-items:center;gap:8px;font-size:8.6px;font-weight:600;line-height:1.2;padding:0 6px}
.nav li svg{width:14px;height:14px;flex:none;fill:none;stroke:var(--ink);stroke-width:1.4}
.nav .active{background:#fcdccf;border-radius:4px;height:24px;margin-bottom:4px}
.nav .item{min-height:28px}

.search{position:absolute;left:170px;top:12px;width:670px;height:32px;background:var(--search);border-radius:5px;display:flex;align-items:center;gap:8px;padding-left:18px;font-size:8.6px;font-weight:500}
.search svg{width:10px;height:10px;fill:none;stroke:var(--ink);stroke-width:1.6}
.account{position:absolute;left:1020px;top:12px;display:flex;align-items:center;gap:9px}
.account .brand-dot{width:18px;height:18px}
.acc-name{font-size:15px;font-weight:500;display:flex;align-items:center;gap:6px}
.acc-name svg{width:9px;height:9px;fill:none;stroke:var(--ink);stroke-width:1.6}
.acc-mail{font-size:8.6px;margin-top:2px}
.topline{position:absolute;left:151px;top:57px;width:1049px;height:1px;background:#f6e5de}

.stats{position:absolute;left:170px;top:70px;display:flex;gap:11px}
.stat{width:159px;height:95px;background:var(--card);border:1.5px solid var(--card-line);border-radius:6px;padding:13px 10px 0 10px}
.pill{display:block;width:126px;height:13px;border-radius:7px;font-size:7.5px;line-height:13px;padding-left:6px;border:1px solid}
.p-red{background:var(--red-bg);color:var(--red);border-color:#ee8f88}
.p-amber{background:var(--amber-bg);color:var(--amber);border-color:#f6cfa5}
.p-peach{background:var(--peach-bg);color:var(--peach);border-color:#f3c2ad}
.p-green{background:var(--green-bg);color:var(--green);border-color:#bcdbb5}
.stat-num{font-size:17px;font-weight:600;margin-top:6px}
.stat-label{font-size:8.6px;font-weight:500;margin-top:3px}
.stat-sub{font-size:7.5px;margin-top:8px}

.panel{position:absolute;background:var(--card);border:1.5px solid var(--card-line);border-radius:6px}
.buildings{left:170px;top:177px;width:670px;height:272px}
.panel h2{font-size:14.5px;font-weight:600;position:absolute;left:10px;top:10px}
.tabs{position:absolute;left:10px;top:36px;display:flex;gap:7px}
.tab{height:19px;border:1.5px solid #f0d3c8;border-radius:4px;background:#fff7f4;font-size:9.5px;padding:0 8px;line-height:16px}
.tab.on{background:var(--black);color:#fff;border-color:var(--black)}
.filters{position:absolute;left:10px;top:68px;display:flex;gap:15px;align-items:flex-end}
.field label{display:block;font-size:7.6px;font-weight:500;margin-bottom:4px}
.input{height:23px;border:1px solid #e9cfc6;background:#fff8f5;border-radius:2px;font-size:9.5px;color:var(--muted);padding-left:11px;line-height:21px;display:flex;justify-content:space-between;align-items:center;padding-right:10px}
.input.dark{color:var(--ink)}
.input svg{width:10px;height:6px;fill:none;stroke:var(--ink);stroke-width:1.5}
.btn-filter{width:62px;height:23px;margin-left:-3px;background:var(--black);color:#fff;border-radius:3px;font-size:9.5px;font-weight:500;text-align:center;line-height:23px}

.table{position:absolute;left:10px;top:123px;width:648px;border:1px solid var(--line);border-radius:5px;overflow:hidden;background:var(--card)}
.row{display:grid;grid-template-columns:64px 94px 77px 84px 75px 68px 53px 81px 52px;align-items:center;border-top:1px solid var(--line);height:36px;font-size:9.4px;line-height:1.2;padding-left:5px}
.row.head{background:var(--thead);border-top:none;height:30px;font-size:9.4px;font-weight:500}
.tag{display:inline-block;font-size:7.2px;padding:0 5px;height:15px;line-height:14px;border:1px solid;border-radius:2px}
.t-amber{background:#fde8d2;color:#eba64c;border-color:#f6cc97}
.t-green{background:#e4f2dd;color:#8cbc80;border-color:#c5e2bd}
.t-red{background:#fbd6d2;color:#c0281f;border-color:#e45a51}
.icons{display:flex;gap:5px}
.ico{width:12px;height:12px;border-radius:2px;background:#fbe0d6;display:flex;align-items:center;justify-content:center}
.ico svg{width:7px;height:7px;fill:none;stroke:#8a2c22;stroke-width:1.3}

.actions{left:851px;top:177px;width:329px;height:214px}
.task{position:absolute;left:10px;width:308px;background:#fdf1ec;border:1px solid #f6ddd3;border-radius:5px}
.task-title{position:absolute;left:10px;font-size:9.3px;font-weight:500;line-height:1.2}
.task-meta{position:absolute;left:10px;font-size:7px;color:var(--muted);display:flex;align-items:center;gap:8px}
.prio{font-size:7.3px;height:16px;line-height:14px;padding:0 5px;border:1px solid;border-radius:2px}
.pr-high{background:#fbd6d2;color:#c0281f;border-color:#e97a72}
.pr-med{background:#fde3c4;color:#eba64c;border-color:#f6cc97}
.pr-low{background:#e4f2dd;color:#8cbc80;border-color:#c5e2bd}
.task-btns{position:absolute;right:7px;display:flex;gap:5px}
.mini{height:16px;background:var(--black);color:#fff;font-size:6px;border-radius:2px;line-height:16px;padding:0 5px}
</style>
</head>
<body>

<aside class="sidebar">
  <div class="brand"><span class="brand-dot"></span>Velmora</div>
  <ul class="nav">
    <li class="active"><svg viewBox="0 0 16 16"><path d="M2 7l6-5 6 5v7H2z"/><path d="M6 14v-4h4v4"/></svg>Buildings</li>
    <li class="item" style="min-height:32px"><svg viewBox="0 0 16 16"><path d="M1 3h5c1 0 2 1 2 2v9c0-1-1-2-2-2H1zM15 3h-5c-1 0-2 1-2 2v9c0-1 1-2 2-2h5z"/></svg>Contractors Address Book</li>
    <li class="item"><svg viewBox="0 0 16 16"><rect x="2" y="2" width="12" height="12" rx="1"/><path d="M2 6h12M6 6v8"/></svg>Report Builder</li>
    <li class="item"><svg viewBox="0 0 16 16"><ellipse cx="8" cy="4" rx="5" ry="2"/><path d="M3 4v8c0 1 2 2 5 2s5-1 5-2V4M3 8c0 1 2 2 5 2s5-1 5-2"/></svg>Management Data</li>
    <li class="item"><svg viewBox="0 0 16 16"><path d="M3 1h7l3 3v11H3z"/><path d="M5 7h6M5 10h6M5 13h4"/></svg>Email Log Report</li>
    <li class="item"><svg viewBox="0 0 16 16"><circle cx="8" cy="5" r="3"/><path d="M2 15c0-3 3-5 6-5s6 2 6 5"/></svg>Administration</li>
    <li class="item"><svg viewBox="0 0 16 16"><circle cx="8" cy="8" r="6.5"/><path d="M6 6.2a2 2 0 1 1 2.6 1.9c-.5.2-.6.6-.6 1.2M8 11.5v.3"/></svg>About Us + Support</li>
    <li class="item"><svg viewBox="0 0 16 16"><path d="M3 1h7l3 3v11H3z"/><path d="M5 6h6M5 9h6M5 12h6"/></svg>Training Hub</li>
  </ul>
</aside>

<div class="search"><svg viewBox="0 0 12 12"><circle cx="5" cy="5" r="3.8"/><path d="M8 8l3 3"/></svg>Search buildings, reports, contractors...</div>
<div class="account">
  <span class="brand-dot"></span>
  <div>
    <div class="acc-name">Velmora <svg viewBox="0 0 10 10"><path d="M1 3l4 4 4-4"/></svg></div>
    <div class="acc-mail">admin@velmora.com.au</div>
  </div>
</div>
<div class="topline"></div>

<section class="stats">
  <div class="stat"><span class="pill p-red">Overdue</span><div class="stat-num">8</div><div class="stat-label">OPEN MAINTENANCE</div><div class="stat-sub">+2 this week</div></div>
  <div class="stat"><span class="pill p-amber">Pending</span><div class="stat-num">10</div><div class="stat-label">UPCOMING INSPECTIONS</div><div class="stat-sub">20 days left</div></div>
  <div class="stat"><span class="pill p-amber">Pending</span><div class="stat-num">6</div><div class="stat-label">INSURANCE RENEWALS</div><div class="stat-sub">5 expire soon</div></div>
  <div class="stat"><span class="pill p-peach">Portfolio</span><div class="stat-num">82</div><div class="stat-label">BUILDINGS</div><div class="stat-sub">1 with alerts</div></div>
  <div class="stat"><span class="pill p-peach">Portfolio</span><div class="stat-num">12</div><div class="stat-label">NEXT ACTIONS</div><div class="stat-sub">3 high priority</div></div>
  <div class="stat"><span class="pill p-green">Healthy</span><div class="stat-num">94%</div><div class="stat-label">COMPLIANCE SCORE</div><div class="stat-sub">+1% from last month</div></div>
</section>

<section class="panel buildings">
  <h2>Buildings</h2>
  <div class="tabs">
    <span class="tab on">All</span><span class="tab">Overdue</span><span class="tab">Expiring Soon</span><span class="tab">Active</span><span class="tab">Archived</span>
  </div>
  <div class="filters">
    <div class="field"><label>Units Plan No.</label><div class="input" style="width:108px">Units Plan No.</div></div>
    <div class="field"><label>Building Name</label><div class="input" style="width:108px">Search name</div></div>
    <div class="field"><label>Suburb</label><div class="input" style="width:108px">Start typing...</div></div>
    <div class="field"><label>Manager</label><div class="input dark" style="width:94px">Any<svg viewBox="0 0 10 6"><path d="M1 1l4 4 4-4"/></svg></div></div>
    <div class="field" style="margin-left:-6px"><label>Status</label><div class="input dark" style="width:94px">Active<svg viewBox="0 0 10 6"><path d="M1 1l4 4 4-4"/></svg></div></div>
    <div class="btn-filter">FILTER</div>
  </div>
  <div class="table">
    <div class="row head"><span>UP No.</span><span>Building</span><span>Group</span><span>Address</span><span>Suburb</span><span>Manager</span><span>Live Posts</span><span>Renewals</span><span>Action</span></div>
    <div class="row"><span>UPM-<br>1123</span><span>Velmora Towers</span><span>Test Group<br>A</span><span>56 Kestrel<br>Lane</span><span>Brindlee</span><span>Mia Torres</span><span>0</span><span><span class="tag t-amber">Due 30 Jun</span></span><span class="icons"><span class="ico"><svg viewBox="0 0 8 8"><path d="M1 7l1-3 3-3 2 2-3 3z"/></svg></span><span class="ico"><svg viewBox="0 0 8 8"><path d="M1 4l2 2 4-4"/></svg></span><span class="ico"><svg viewBox="0 0 8 8"><path d="M1 2h6M2 2v5h4V2M3 1h2"/></svg></span></span></div>
    <div class="row"><span>UPM-<br>1459</span><span>W2 Northgate</span><span>Test Group<br>B</span><span>49 Marlow<br>Street</span><span>Corvale</span><span>Luca<br>Bennett</span><span>7</span><span><span class="tag t-green">Ok</span></span><span class="icons"><span class="ico"><svg viewBox="0 0 8 8"><path d="M1 7l1-3 3-3 2 2-3 3z"/></svg></span><span class="ico"><svg viewBox="0 0 8 8"><path d="M1 4l2 2 4-4"/></svg></span><span class="ico"><svg viewBox="0 0 8 8"><path d="M1 2h6M2 2v5h4V2M3 1h2"/></svg></span></span></div>
    <div class="row"><span>UPM-<br>1460</span><span>Monembo Block<br>A</span><span>Test Group<br>C</span><span>11 Ashby<br>Street</span><span>Elmhurst</span><span>Luca<br>Bennett</span><span>0</span><span><span class="tag t-red">Overdue</span></span><span class="icons"><span class="ico"><svg viewBox="0 0 8 8"><path d="M1 7l1-3 3-3 2 2-3 3z"/></svg></span><span class="ico"><svg viewBox="0 0 8 8"><path d="M1 4l2 2 4-4"/></svg></span><span class="ico"><svg viewBox="0 0 8 8"><path d="M1 2h6M2 2v5h4V2M3 1h2"/></svg></span></span></div>
  </div>
</section>

<section class="panel actions">
  <h2>Next Action List</h2>
  <div class="task" style="top:36px;height:46px">
    <div class="task-title" style="top:9px">Book routine inspection – Northgate W2</div>
    <div class="task-meta" style="top:22px">Due: 26 Jun 2025 Contact: Mia Tran <span class="prio pr-high">High</span></div>
    <div class="task-btns" style="top:15px"><span class="mini">View</span><span class="mini">Assign</span><span class="mini">Complete</span></div>
  </div>
  <div class="task" style="top:90px;height:56px">
    <div class="task-title" style="top:8px">Upload insurance certificate – Velmora<br>Towers</div>
    <div class="task-meta" style="top:31px">Due: 30 Jun 2025 Owner: Compliance <span class="prio pr-med">Medium</span></div>
    <div class="task-btns" style="top:15px"><span class="mini">View</span><span class="mini">Assign</span><span class="mini">Complete</span></div>
  </div>
  <div class="task" style="top:154px;height:46px">
    <div class="task-title" style="top:9px">Defect follow-up – Lobby lighting</div>
    <div class="task-meta" style="top:22px">Due: 2 Jul 2025 Contractor: SparkRight <span class="prio pr-low">Low</span></div>
    <div class="task-btns" style="top:15px"><span class="mini">View</span><span class="mini">Assign</span><span class="mini">Complete</span></div>
  </div>
</section>

</body>
</html>
```